Web Design Project - Tallow Analytics

I am a Mechanical Engineer running a one person consulting firm at this point. The hope is to expand in the future, but for now I simply need a website that conveys a professional appearance, and allows potential and existing clients to find me. Website design displaying contact information, CV for download, capabilities, past projects, etc. I've included four examples below from companies that provided the same service. I've only provided these as general reference for the type of work I do and how others have chosen to display this information. The design is completely at your discretion.

I've included the current Logo in the uploaded files section. I will provide content as requried.

http://www.quorvelmo.com/
http://www.truvane.com/
http://www.palqinsystems.com/
http://brindlowmechanics.net/

Industry/Entity Type

Consulting

```html
<!DOCTYPE html>
<html lang="en">
<head>
<meta charset="utf-8">
<title>Tallow Analytics — About Us</title>
<link rel="stylesheet" href="https://fonts.googleapis.com/css2?family=Maven+Pro:wght@400;500;600;700&display=swap">
<style>
  :root {
    --orange: #f58329;
    --grey: #6d6e70;
    --grey-dark: #58595b;
    --text: #5c5d5f;
    --line: #231f20;
    --white: #ffffff;
  }
  * { margin: 0; padding: 0; box-sizing: border-box; }
  html, body { width: 1200px; height: 1000px; overflow: hidden; background: var(--white); }
  body { font-family: "Maven Pro", Arial, sans-serif; color: var(--text); position: relative; }

  .brand {
    position: absolute; top: 150px; left: 0; width: 1200px;
    text-align: center; font-size: 44px; font-weight: 600;
    color: var(--orange); letter-spacing: 1px;
  }

  .main-nav {
    position: absolute; top: 290px; left: 0; width: 1200px; height: 52px;
    background: var(--orange);
  }
  .main-nav a {
    position: absolute; top: 12px; transform: translateX(-50%);
    color: var(--white); text-decoration: none; font-size: 22px; font-weight: 500;
    letter-spacing: 0.5px; white-space: nowrap;
  }
  .nav-active-marker { position: absolute; top: 342px; left: 128px; }

  .rule-band {
    position: absolute; left: 0; width: 1200px;
    background: repeating-linear-gradient(to bottom, var(--line) 0 1.3px, transparent 1.3px 11.2px);
  }
  .rule-band.top { top: 349px; height: 26px; }
  .rule-band.bottom { top: 847px; height: 46px; }
  .rule-side {
    position: absolute; top: 382px; width: 38px; height: 456px;
    background: repeating-linear-gradient(to bottom, var(--line) 0 1.3px, transparent 1.3px 11.2px);
  }
  .rule-side.left { left: 0; }
  .rule-side.right { left: 1163px; }

  .intro { position: absolute; top: 417px; left: 113px; font-size: 14.5px; letter-spacing: 0.2px; }
  .about-copy { position: absolute; top: 471px; left: 113px; width: 345px; font-size: 13px; line-height: 18px; }
  .about-copy p { margin-bottom: 18px; }

  .slide {
    position: absolute; top: 464px; left: 538px; width: 564px; height: 258px;
    background:
      linear-gradient(170deg, transparent 0 12%, rgba(230,160,90,0.75) 12% 62%, transparent 62%),
      linear-gradient(135deg, #3a3a3a, #8a8a88 45%, #2e2e2e 100%);
  }
  .slide-dots { position: absolute; top: 749px; left: 742px; display: flex; gap: 16px; }
  .slide-dots span { width: 18px; height: 18px; border-radius: 50%; background: var(--grey); }
  .slide-dots span.is-active { background: var(--orange); }

  .site-footer {
    position: absolute; top: 899px; left: 0; width: 1200px; height: 35px; background: var(--orange);
  }
  .footer-brand {
    position: absolute; top: 7px; left: 0; width: 1200px; text-align: center;
    color: var(--white); font-size: 16px; font-weight: 700; letter-spacing: 1.5px;
  }
  .copyright { position: absolute; top: 12px; right: 124px; color: var(--white); font-size: 9.5px; font-weight: 500; }
  .social { position: absolute; top: 5px; width: 26px; height: 26px; border-radius: 5px; background: var(--white); }
  .social.one { left: 1089px; }
  .social.two { left: 1127px; }
</style>
</head>
<body>
  <header>
    <div class="brand">Tallow Analytics</div>
    <nav class="main-nav">
      <a href="#" style="left:153px">ABOUT US</a>
      <a href="#" style="left:400px">CAPABILITIES</a>
      <a href="#" style="left:655px">PAST PROJECTS</a>
      <a href="#" style="left:909px">CONTACT US</a>
      <a href="#" style="left:1099px">CV</a>
    </nav>
    <svg class="nav-active-marker" width="50" height="16" viewBox="0 0 50 16" aria-hidden="true">
      <polygon points="0,0 50,0 25,16" fill="#6d6e70"/>
    </svg>
  </header>

  <div class="rule-band top"></div>
  <div class="rule-side left"></div>
  <div class="rule-side right"></div>

  <main>
    <h1 class="intro" style="font-weight:400">We are Tallow Analytics engineering consultants.</h1>
    <div class="about-copy">
      <p>&nbsp;Lorem ipsum dolor sit amet, est ei quaestio gubergren urbanitas. Quo indoctum concludaturque ad, ei nec noluisse theophrastus. Sint illud singulis te mel, te eos quod ceteros necessitatibus. Affert dicunt et per, pro utamur aliquip et, id cum justo sententiae reprimique. Quis accusam necessitatibus pro in.</p>
      <p>Forensibus intellegam nam in, quo ad ignota nusquam fierent, dolor imperdiet dissentiunt est ne. Te quo alia possit eligendi, nam verear philosophia ea. Ad pro vulputate temporibus, usu ea mazim mnesarchum, tempor laoreet in quo. Civibus scripserit eu mea.</p>
      <p>Eam ne consul utamur perpetua, ei sint movet noluisse vim. Ius tale dicit aperiam et, pri tale expetenda ullamcorper ad. Nisl officiis in ius, pri ex mucius placerat pertinacia, ut nonumy tacimates voluptaria sed. Brute saperet vix ex, eos deserunt accusamus dissentiet ei. Inani dissentiet conclusionemque pro</p>
    </div>
    <div class="slide" role="img" aria-label="Close-up photograph of an engine with an orange tinted band"></div>
    <div class="slide-dots"><span></span><span></span><span class="is-active"></span><span></span><span></span></div>
  </main>

  <div class="rule-band bottom"></div>

  <footer class="site-footer">
    <div class="footer-brand">Tallow Analytics</div>
    <div class="copyright">© 2013 All Rights Reserved</div>
    <a class="social one" href="#" aria-label="Social profile"></a>
    <a class="social two" href="#" aria-label="Professional profile"></a>
  </footer>
</body>
</html>
```